Web page update/ Create new non flash site

I have a flash web page, created by my ex girlfriend through some kind of web design service. I want to take all of the information that I have on the page and put it together in a similar manner on a non-flash page.I want to add a lot of pictures, update the logo to the one i had made on pixel bazaar and reword a few things to reflect the the direction my business has gone in, in the past couple years since I made the site.. I also can't figure out why when people e-mail me from my page, I get the e-mail but no message, happens all the time and makes me think I'm losing business. My main problem is that I don't know what service was used in the past to create this page or what information someone would need to be able to work on it more. I also have another domain name that I want connected to it. the existing web page is at www.quillbyconstruction.net

Target Market(s)

I originally made this web page thinking that i was going to be in the remodeling business, but the majority of the work i get is for high end commercial and residential millwork and carpentry installations. I mainly will be advertising to other general contractors, but I want to keep the same feel that it has now, how it is mainly talking to homeowners that are thinking about hiring me to do some sort of project for them.

Industry/Entity Type

Business

Requirements
Must have
• Portfolio page needs to be updated to have LOTS more pictures and have them in an organized manner where it's easy to navigate through them. My other main thing is that I want to keep the same look and feel that it has with the nice woodgrain background, user friendly layout of links, etc.

```html
<!DOCTYPE html>
<html lang="en">
<head>
<meta charset="utf-8">
<title>Quillby Construction</title>
<link href="https://fonts.googleapis.com/css2?family=Comfortaa:wght@400;700&family=Cabin:wght@400;500&display=swap" rel="stylesheet">
<style>
:root{
  --wood-1:#4a3020;
  --wood-2:#5a3a26;
  --wood-3:#3e271a;
  --panel:rgba(40,24,14,.35);
  --panel-edge:rgba(20,10,4,.7);
  --cream:#f1e3c8;
  --text:#eadbc2;
  --paper:#e9dcae;
  --paper-dark:#cbbb86;
  --ink:#4a3322;
}
*{margin:0;padding:0;box-sizing:border-box}
html,body{width:956px;height:1200px;overflow:hidden}
body{
  position:relative;
  font-family:"Cabin",sans-serif;
  color:var(--text);
  background:
    repeating-linear-gradient(90deg,rgba(0,0,0,.08) 0 3px,rgba(255,255,255,.03) 3px 7px,rgba(0,0,0,.05) 7px 12px,transparent 12px 19px),
    repeating-linear-gradient(90deg,var(--wood-1) 0 40px,var(--wood-2) 40px 70px,var(--wood-3) 70px 95px,var(--wood-1) 95px 130px);
}
.abs{position:absolute}
.panel{position:absolute;background:var(--panel);border:1px solid var(--panel-edge);border-radius:8px;
  box-shadow:inset 0 0 14px rgba(0,0,0,.45),0 1px 0 rgba(255,255,255,.08)}
.brand{left:96px;top:22px;font-family:"Comfortaa",sans-serif;font-size:36px;color:var(--cream);letter-spacing:.5px}
.tagline{left:214px;top:70px;font-family:"Comfortaa",sans-serif;font-size:14px;color:var(--cream)}
.nav-btn{position:absolute;left:102px;width:149px;height:40px;background:linear-gradient(180deg,var(--paper),var(--paper-dark));
  color:var(--ink);font-family:"Comfortaa",sans-serif;font-weight:700;font-size:15px;display:flex;align-items:center;justify-content:center;
  clip-path:polygon(0 6%,40% 0,100% 3%,99% 50%,100% 96%,55% 100%,1% 97%,0 50%);box-shadow:0 2px 3px rgba(0,0,0,.5)}
.photo{position:absolute;border-radius:1px}
.hero{left:291px;top:123px;width:557px;height:283px;background:linear-gradient(135deg,#e9d3a4 0%,#9a5b2c 40%,#6e3d1d 70%,#3a2212 100%);border:1px solid #d8c5a4}
.thumb{top:463px;width:101px;height:78px;border:2px solid #efe6dc}
.arrow{position:absolute;top:483px}
.h2{position:absolute;font-family:"Comfortaa",sans-serif;color:var(--cream);white-space:nowrap}
.services-list{position:absolute;left:100px;top:623px;list-style:none;font-size:11px}
.services-list li{height:23.3px;display:flex;align-items:center;gap:8px}
.more{position:absolute;font-family:"Comfortaa",sans-serif;font-size:11px;color:var(--cream)}
.welcome-text{position:absolute;left:356px;top:625px;width:267px;font-size:11.4px;line-height:16.6px;text-align:justify}
.box-text{position:absolute;font-family:"Comfortaa",sans-serif;font-size:9px;line-height:12.8px;width:212px}
.quote{position:absolute;left:642px;top:880px;width:215px;font-size:10.5px;line-height:16.6px}
.footer-links{position:absolute;left:81px;width:779px;top:1110px;text-align:center;font-size:11.5px;word-spacing:2px}
.footer-links span{margin:0 8px}
.copyright{position:absolute;left:81px;width:779px;top:1136px;text-align:center;font-size:11px}
</style>
</head>
<body>
<header>
  <div class="abs brand">Quillby Construction</div>
  <div class="abs tagline">building and rennovation company</div>
</header>

<section class="panel" style="left:83px;top:103px;width:780px;height:325px"></section>
<nav>
  <div class="nav-btn" style="top:126px">Home</div>
  <div class="nav-btn" style="top:174px">About Us</div>
  <div class="nav-btn" style="top:222px">Services</div>
  <div class="nav-btn" style="top:270px">Portfolio</div>
  <div class="nav-btn" style="top:318px">Process</div>
  <div class="nav-btn" style="top:367px">Contact</div>
</nav>
<div class="photo hero" role="img" aria-label="Warm kitchen and dining room interior with chandelier"></div>

<section class="panel" style="left:83px;top:445px;width:780px;height:114px"></section>
<svg class="arrow" style="left:89px" width="22" height="26" viewBox="0 0 22 26"><path d="M17 3 L6 13 L17 23" fill="none" stroke="#efe3cf" stroke-width="5"/></svg>
<svg class="arrow" style="left:834px" width="22" height="26" viewBox="0 0 22 26"><path d="M5 3 L16 13 L5 23" fill="none" stroke="#efe3cf" stroke-width="5"/></svg>
<div class="photo thumb" style="left:124px;background:linear-gradient(135deg,#c9a676,#6a4a30)" role="img" aria-label="Living room with fireplace"></div>
<div class="photo thumb" style="left:241px;background:linear-gradient(135deg,#8aa0ad,#c8c2b8)" role="img" aria-label="Bedroom with blue walls"></div>
<div class="photo thumb" style="left:360px;background:linear-gradient(135deg,#a88650,#2e1f16)" role="img" aria-label="Living room with piano"></div>
<div class="photo thumb" style="left:478px;background:linear-gradient(135deg,#6a4b3a,#c79a6a)" role="img" aria-label="Dining room with curtains"></div>
<div class="photo thumb" style="left:598px;background:linear-gradient(135deg,#b39a7a,#5a4030)" role="img" aria-label="Bedroom with dark pillows"></div>
<div class="photo thumb" style="left:716px;background:linear-gradient(135deg,#c07a4a,#5a2f1c)" role="img" aria-label="Dining room with chandelier"></div>

<section class="panel" style="left:83px;top:576px;width:248px;height:220px"></section>
<div class="h2" style="left:101px;top:586px;font-size:19px">Services</div>
<ul class="services-list">
  <li><svg width="11" height="10" viewBox="0 0 11 10"><rect x=".5" y="2.5" width="7" height="7" fill="none" stroke="#eadbc2"/><path d="M2 5 L4 8 L10 1" fill="none" stroke="#eadbc2" stroke-width="2"/></svg>Bathrooms</li>
  <li><svg width="11" height="10" viewBox="0 0 11 10"><rect x=".5" y="2.5" width="7" height="7" fill="none" stroke="#eadbc2"/><path d="M2 5 L4 8 L10 1" fill="none" stroke="#eadbc2" stroke-width="2"/></svg>Custom Cabinetry</li>
  <li><svg width="11" height="10" viewBox="0 0 11 10"><rect x=".5" y="2.5" width="7" height="7" fill="none" stroke="#eadbc2"/><path d="M2 5 L4 8 L10 1" fill="none" stroke="#eadbc2" stroke-width="2"/></svg>Frame and Finish Carpentry</li>
  <li><svg width="11" height="10" viewBox="0 0 11 10"><rect x=".5" y="2.5" width="7" height="7" fill="none" stroke="#eadbc2"/><path d="M2 5 L4 8 L10 1" fill="none" stroke="#eadbc2" stroke-width="2"/></svg>Outdoor Living and Decks</li>
  <li><svg width="11" height="10" viewBox="0 0 11 10"><rect x=".5" y="2.5" width="7" height="7" fill="none" stroke="#eadbc2"/><path d="M2 5 L4 8 L10 1" fill="none" stroke="#eadbc2" stroke-width="2"/></svg>Energy Efficient/Green Remodeling</li>
  <li><svg width="11" height="10" viewBox="0 0 11 10"><rect x=".5" y="2.5" width="7" height="7" fill="none" stroke="#eadbc2"/><path d="M2 5 L4 8 L10 1" fill="none" stroke="#eadbc2" stroke-width="2"/></svg>Doors and Windows</li>
  <li><svg width="11" height="10" viewBox="0 0 11 10"><rect x=".5" y="2.5" width="7" height="7" fill="none" stroke="#eadbc2"/><path d="M2 5 L4 8 L10 1" fill="none" stroke="#eadbc2" stroke-width="2"/></svg>Custom Concrete</li>
</ul>
<div class="more" style="left:247px;top:777px">View more [+]</div>

<div class="h2" style="left:356px;top:579px;font-size:18px">Welcome to Quillby Construction</div>
<p class="welcome-text">Welcome to Quillby Construction, a locally owned and operated residential and commercial construction company serving the greater New Orleans area and southeastern Louisiana. We are experts in all forms of residential building, remodeling and renovations.<br><br>architectural styles and being held to the highest quality standards demanded by the residents of Capital Hill and surrounding areas.</p>
<div class="more" style="left:550px;top:794px">View more [+]</div>
<div class="photo" style="left:724px;top:609px;width:136px;height:130px;transform:rotate(8deg);background:linear-gradient(135deg,#1c2440,#6a4226 60%,#d08a3a);border:2px solid #efe6dc" role="img" aria-label="Evening patio with string lights"></div>
<div class="photo" style="left:637px;top:629px;width:140px;height:123px;background:linear-gradient(135deg,#dcd8cc,#8f8a80);border:1px solid #efe6dc" role="img" aria-label="Living room with white fireplace"></div>

<section class="panel" style="left:83px;top:839px;width:248px;height:200px"></section>
<div class="h2" style="left:91px;top:851px;font-size:13.6px;letter-spacing:-.3px">Why Choose Quillby Construction</div>
<div class="photo" style="left:98px;top:879px;width:200px;height:86px;background:linear-gradient(90deg,#5d6670,#7a848c 60%,#b5582c)" role="img" aria-label="Modern house exterior with stairs"></div>
<p class="box-text" style="left:98px;top:970px">At Quillby Construction, we accredit our success to many factors that are evident in all of our work. our core values as a company, which are as follows:</p>
<div class="more" style="left:241px;top:1023px">View more [+]</div>

<section class="panel" style="left:355px;top:839px;width:248px;height:200px"></section>
<div class="h2" style="left:365px;top:848px;font-size:15.5px">Core Values</div>
<div class="photo" style="left:371px;top:874px;width:199px;height:87px;background:linear-gradient(135deg,#cfc6b6,#a2835c 55%,#e8e4dc)" role="img" aria-label="Open kitchen and living area with wood floor"></div>
<p class="box-text" style="left:371px;top:969px">At Quillby Construction, we accredit our success to many factors that are evident in all of our work. our core values as a company, which are as follows:</p>
<div class="more" style="left:515px;top:1023px">View more [+]</div>

<section class="panel" style="left:623px;top:839px;width:248px;height:200px"></section>
<div class="h2" style="left:637px;top:846px;font-size:15.5px">Testimonials</div>
<div class="abs" style="left:628px;top:867px;font-size:20px;font-family:Georgia,serif;color:var(--cream)">&ldquo;</div>
<p class="quote">I have had two great experiences with John Quillby's company during my tenure at Ridgeway Builders.His company first went to work had many challenges for all the subs that worked there.<br>while many of them could not deal with the complex issues without a great deal of hand holding, <b style="font-family:Georgia,serif;font-size:15px">&rdquo;</b></p>
<div class="more" style="left:778px;top:1018px">View more [+]</div>

<footer>
  <section class="panel" style="left:81px;top:1095px;width:779px;height:72px"></section>
  <div class="footer-links">Home<span>|</span>About Us<span>|</span>Services<span>|</span>Portfolio<span>|</span>Process<span>|</span>Contact</div>
  <div class="copyright">Copyright &copy; 2012 Quillby Construction.com . All Rights Reserved.</div>
</footer>
</body>
</html>
```